Author needs a new book, Kindle and Audiobook cover design

I updated and re-edited a book I wrote 25 years ago but now realize the title and design did not get the job done. I am seeking a book, Kindle and audiobook design that will make me stand out. The final design will pop while being sensitive to the nature of the subject. The title of the book is Quiet Lanterns. Subtitle: Ways to Notice and Step Away From Harmful Circles While Keeping Steady Belief by Dorian T. Wexcombe. I am wanting to get the attention of people who have been damaged by a church relationship that started well but ended badly.
Updates

The book title is: Quiet Lanterns. The Subtitle is: Ways To Notice and Step Away From Harmful Circles While Keeping Steady Belief. The dimension is 6x9 (150 pages) and I am the author: Dorian T. Wexcombe

Target Market(s)

People with a church experience; church leadership. Religious abuse victims.

Industry/Entity Type

Christian

Font styles to use
Serif

Colors

Designer to choose colors to be used in the design.

Requirements
Nice to have
• I am not married to the Serif font if another design works better.

```html
<!DOCTYPE html>
<html lang="en">
<head>
<meta charset="utf-8">
<title>Quiet Lanterns — Cover Wrap</title>
<link href="https://fonts.googleapis.com/css2?family=Sancreek&family=Oregano&family=Tinos:wght@400;700&display=swap" rel="stylesheet">
<style>
  :root {
    --back-brown: #8d4626;
    --back-brick: #a85a34;
    --spine-brown: #7c3b1e;
    --ink-dark: #140905;
    --cream: #f6ead8;
    --title-red: #c4121b;
    --subtitle-red: #7e1a10;
    --rule-red: #6e1d0f;
    --white: #ffffff;
  }
  * { margin: 0; padding: 0; box-sizing: border-box; }
  html, body { width: 1200px; height: 863px; overflow: hidden; background: #ddd; }
  .cover-wrap { position: relative; width: 1200px; height: 863px; overflow: hidden; }

  /* Back cover */
  .back-cover {
    position: absolute; left: 0; top: 0; width: 575px; height: 863px;
    background: var(--back-brown);
  }
  .back-texture {
    position: absolute; left: 0; top: 0; width: 575px; height: 863px;
    background: radial-gradient(ellipse at 20% 15%, var(--back-brick) 0%, rgba(168,90,52,0.4) 40%, rgba(141,70,38,0) 75%);
  }
  .back-title-block {
    position: absolute; left: 40px; top: 58px; width: 170px; text-align: center;
    color: var(--cream);
  }
  .back-title {
    font-family: "Sancreek", serif; font-weight: 400; font-size: 38px; line-height: 46px;
  }
  .back-subtitle {
    margin-top: 8px; font-family: "Oregano", cursive; font-size: 14px; line-height: 20.5px;
  }
  .endorsements {
    position: absolute; left: 37px; top: 37px; width: 503px;
    font-family: "Tinos", serif; font-size: 13.8px; line-height: 17.5px;
    color: var(--ink-dark); text-align: justify;
  }
  .endorsements .title-space { float: left; width: 179px; height: 228px; }
  .endorsements p { margin: 0; }
  .back-rule {
    position: absolute; left: 37px; top: 504px; width: 503px; height: 2px;
    background: linear-gradient(90deg, rgba(110,29,15,0.3), var(--rule-red) 20%, var(--rule-red) 80%, rgba(110,29,15,0.3));
  }
  .author-photo {
    position: absolute; left: 37px; top: 532px; width: 126px; height: 175px;
    background: linear-gradient(180deg, #1c1d24 0%, #3a3e4a 60%, #4a5575 100%);
  }
  .author-bio {
    position: absolute; left: 216px; top: 530px; width: 324px;
    font-family: "Tinos", serif; font-size: 13.8px; line-height: 17.5px;
    color: var(--ink-dark); text-align: justify;
  }
  .author-bio strong { font-weight: 700; }

  /* Spine */
  .spine {
    position: absolute; left: 575px; top: 0; width: 50px; height: 863px;
    background: var(--spine-brown);
  }
  .spine-text {
    position: absolute; left: 25px; white-space: nowrap; color: var(--white);
    transform-origin: 0 0; transform: rotate(90deg) translateY(-50%);
  }
  .spine-title { top: 186px; font-family: "Sancreek", serif; font-size: 28px; line-height: 34px; }
  .spine-author { top: 642px; font-family: "Oregano", cursive; font-size: 22px; line-height: 28px; }

  /* Front cover */
  .front-cover { position: absolute; left: 625px; top: 0; width: 575px; height: 863px; }
  .front-art {
    position: absolute; inset: 0;
    background:
      radial-gradient(ellipse 60% 50% at 55% 38%, #d7eef6 0%, #8fc3dd 35%, rgba(143,195,221,0) 70%),
      linear-gradient(180deg, rgba(0,0,0,0) 0%, rgba(0,0,0,0) 42%, #c9cf3a 52%, #a9b82a 75%, #8a9a22 100%),
      linear-gradient(90deg, #c96a3e 0%, #d98455 10%, rgba(217,132,85,0) 24%, rgba(217,132,85,0) 82%, #d7804f 90%, #c05f34 100%),
      #6fa9cb;
  }
  .front-title {
    position: absolute; left: 0; top: 118px; width: 575px; text-align: center;
    font-family: "Sancreek", serif; font-size: 86px; line-height: 100px;
    color: var(--title-red);
    text-shadow: 0 0 3px var(--white), 0 0 6px rgba(255,255,255,0.9), 2px 3px 4px rgba(0,0,0,0.25);
  }
  .front-subtitle {
    position: absolute; left: 20px; top: 343px; width: 360px; text-align: center;
    font-family: "Oregano", cursive; font-size: 22px; line-height: 33px;
    color: var(--subtitle-red);
    text-shadow: 0 0 4px rgba(255,255,255,0.8);
  }
  .front-author {
    position: absolute; left: 0; top: 780px; width: 575px; text-align: center;
    font-family: "Oregano", cursive; font-size: 50px; line-height: 60px;
    color: var(--white);
    text-shadow: 1px 2px 4px rgba(0,0,0,0.6);
  }
</style>
</head>
<body>
<main class="cover-wrap">
  <section class="back-cover">
    <div class="back-texture" role="img" aria-label="Faint red brick wall texture"></div>

    <div class="back-title-block">
      <h2 class="back-title">Quiet<br>Lanterns</h2>
      <p class="back-subtitle">Ways to Notice and Step Away<br>From Harmful Circles While<br>Keeping Steady Belief</p>
    </div>

    <div class="endorsements">
      <div class="title-space"></div>
      <p>Dorian Wexcombe offers expert insight and a transparent evaluation in this book. With years of healthy involvement with that which is right in the body of Christ, he can speak to both the personal and systematic issues that cause bad environments to develop. The church landscape is littered with people who have been hurt in churches. This book will help clean things up. --Martin Oakridge, Senior Pastor, Cedar Hollow Fellowship, Millbrook, VT. cedarhollowfs.org “Seldom, if ever, have I read a book that was so refreshingly personal and real, yet delivered material that put you in a position to navigate the difficult and damaging challenges, of being part of a degenerating church. I was moved to tears and then lifted to a place of hope, by the pain and abuse that this family faced and their incredible testimony and journey of recovery. All glory to the power of His love for us.” -- Pieter Vosloo, Kestrel Outreach, farfieldjourneys.com</p>
      <p>“Dorian Wexcombe offers a real-world view on how following your spiritual calling is not always easy but completely worth the journey. His down to earth approach allows the reader to process and be encouraged by his personal story, insight, and commitment to faith.” Lena Marchetti, Executive Director, Open Table Ministry, Inc. opentablemin.org</p>
      <p>&nbsp;“Dorian Wexcombe has been a pastor over 40 years. I have known him personally for many of those years. This book is a case study of how trust can be abused. Dorian handles this difficult issue with a good balance of honest introspection and critical analysis of leadership structures and practices. This book is a must-read.” --Owen R. Talbot, reasonedhope.net</p>
    </div>

    <div class="back-rule"></div>

    <div class="author-photo" role="img" aria-label="Author portrait photograph"></div>
    <p class="author-bio"><strong>DORIAN WEXCOMBE</strong> is a long-time pastor, author and podcaster who has impacted leaders and churches for many years. He wrote Hull Breach, a study of church leadership drawn from the history of the legendary ship. He and his wife Marguerite, together with their grown children and spouses all serve in ministry.</p>
  </section>

  <section class="spine">
    <div class="spine-text spine-title">Quiet Lanterns</div>
    <div class="spine-text spine-author">Dorian T. Wexcombe</div>
  </section>

  <section class="front-cover">
    <div class="front-art" role="img" aria-label="Photograph of a person standing in a green field, seen through a broken hole in a red brick wall under a blue sky"></div>
    <h1 class="front-title">Quiet<br>Lanterns</h1>
    <p class="front-subtitle">Ways to Notice and Step Away<br>From Harmful Circles While<br>Keeping Steady Belief</p>
    <p class="front-author">Dorian T. Wexcombe</p>
  </section>
</main>
</body>
</html>
```